hobby beef jerky maker looking to break into the commercial market

We need product labels designed for each flavour of jerky we make. Currently have 3 flavours that we are ready to share with the world. We need in your face designs to help us stand out from an already crowded market.
The product name is Rivet Beef Jerky.
The flavours we offer have been named Porch Lope, Ember Glaze and Chili Knack.
The Rivet Beef Jerky Title should remain the same across the three labels but the design for each flavour can change as you see fit.
Label needs to fit within 110mm x 110mm to suit our current packaging

Industry/Entity Type

Food Production

Logo Text

Morvendale Apiary

Colors

Designer to choose colors to be used in the design.

Requirements
Must have
• "Rivet Beef Jerky" font and colour must remain the same across the 3 designs
Nice to have
• The labels will be used on the clear side of the packaging with a small space towards the bottom being left visible so the product inside can be seen

```html
<!DOCTYPE html>
<html lang="en">
<head>
<meta charset="utf-8">
<title>Rivet Beef Jerky – Flavour Labels</title>
<link rel="stylesheet" href="https://fonts.googleapis.com/css2?family=Cinzel:wght@700&family=Permanent+Marker&display=swap">
<style>
  :root {
    --canvas-bg: #ebe6de;
    --pouch-black: #0d0d0d;
    --brand-red: #c8202c;
    --band-red: #b8141f;
    --gold: #e3c98f;
    --ink-dark: #1a1111;
    --jerky-dark: #4a1a12;
    --jerky-mid: #7a3020;
    --mark-red: #8e1019;
  }
  * { box-sizing: border-box; margin: 0; padding: 0; }
  html, body { width: 1200px; height: 1000px; overflow: hidden; }
  body { background: var(--canvas-bg); position: relative; }

  .pouch {
    position: absolute;
    background: var(--pouch-black);
    border-radius: 6px;
    overflow: hidden;
  }
  .pouch--chili { left: 40px; top: 178px; width: 370px; height: 540px; z-index: 1; }
  .pouch--porch { left: 392px; top: 232px; width: 414px; height: 598px; z-index: 2; }
  .pouch--ember { left: 786px; top: 172px; width: 377px; height: 548px; z-index: 1; }

  .brand-mark {
    position: absolute;
    left: 50%;
    transform: translateX(-50%);
    border-radius: 50%;
    background: var(--mark-red);
  }
  .pouch--chili .brand-mark { top: 70px; width: 104px; height: 104px; }
  .pouch--porch .brand-mark { top: 100px; width: 120px; height: 120px; }
  .pouch--ember .brand-mark { top: 64px; width: 106px; height: 106px; }

  .brand-name {
    position: absolute;
    left: 0; right: 0;
    text-align: center;
    font-family: "Cinzel", serif;
    font-weight: 700;
    color: var(--brand-red);
    line-height: 1.05;
  }
  .pouch--chili .brand-name { top: 196px; font-size: 38px; }
  .pouch--porch .brand-name { top: 240px; font-size: 42px; }
  .pouch--ember .brand-name { top: 192px; font-size: 38px; }

  .flavour-band {
    position: absolute;
    left: 0; right: 0;
    border-top: 2px solid var(--gold);
    border-bottom: 2px solid var(--gold);
    display: flex;
    align-items: center;
    justify-content: center;
    font-family: "Permanent Marker", cursive;
    letter-spacing: 1px;
  }
  .pouch--chili .flavour-band { top: 309px; height: 55px; background: var(--pouch-black); color: var(--brand-red); font-size: 30px; }
  .pouch--porch .flavour-band { top: 323px; height: 98px; background: var(--band-red); color: var(--gold); font-size: 36px; }
  .pouch--ember .flavour-band { top: 295px; height: 88px; background: var(--band-red); color: var(--ink-dark); font-size: 32px; }

  .product-window {
    position: absolute;
    left: 0;
    width: 100%;
  }
  .pouch--chili .product-window { top: 366px; height: 160px; }
  .pouch--porch .product-window { top: 423px; height: 165px; }
  .pouch--ember .product-window { top: 385px; height: 145px; }
</style>
</head>
<body>

  <section class="pouch pouch--chili">
    <div class="brand-mark"></div>
    <h1 class="brand-name">Rivet<br>Beef Jerky</h1>
    <div class="flavour-band">Chili Knack</div>
    <svg class="product-window" viewBox="0 0 370 160" preserveAspectRatio="none" role="img" aria-label="Clear window showing strips of beef jerky inside the pouch">
      <defs>
        <linearGradient id="jerky-chili" x1="0" y1="0" x2="1" y2="1">
          <stop offset="0" stop-color="var(--jerky-dark)"/>
          <stop offset="0.5" stop-color="var(--jerky-mid)"/>
          <stop offset="1" stop-color="var(--jerky-dark)"/>
        </linearGradient>
      </defs>
      <polygon points="30,0 345,0 250,150 175,158 130,150" fill="url(#jerky-chili)"/>
    </svg>
  </section>

  <section class="pouch pouch--porch">
    <div class="brand-mark"></div>
    <h1 class="brand-name">Rivet<br>Beef Jerky</h1>
    <div class="flavour-band">Porch Lope</div>
    <svg class="product-window" viewBox="0 0 414 165" preserveAspectRatio="none" role="img" aria-label="Clear window showing strips of beef jerky inside the pouch">
      <defs>
        <linearGradient id="jerky-porch" x1="0" y1="0" x2="1" y2="1">
          <stop offset="0" stop-color="var(--jerky-dark)"/>
          <stop offset="0.5" stop-color="var(--jerky-mid)"/>
          <stop offset="1" stop-color="var(--jerky-dark)"/>
        </linearGradient>
      </defs>
      <polygon points="30,0 385,0 280,150 195,162 145,150" fill="url(#jerky-porch)"/>
    </svg>
  </section>

  <section class="pouch pouch--ember">
    <div class="brand-mark"></div>
    <h1 class="brand-name">Rivet<br>Beef Jerky</h1>
    <div class="flavour-band">Ember Glaze</div>
    <svg class="product-window" viewBox="0 0 377 145" preserveAspectRatio="none" role="img" aria-label="Clear window showing strips of beef jerky inside the pouch">
      <defs>
        <linearGradient id="jerky-ember" x1="0" y1="0" x2="1" y2="1">
          <stop offset="0" stop-color="var(--jerky-dark)"/>
          <stop offset="0.5" stop-color="var(--jerky-mid)"/>
          <stop offset="1" stop-color="var(--jerky-dark)"/>
        </linearGradient>
      </defs>
      <polygon points="30,0 350,0 255,135 180,143 135,135" fill="url(#jerky-ember)"/>
    </svg>
  </section>

</body>
</html>
```